Modernise Business Card

Our company has been operating for 10 years. With the start of the new decade we are looking to refresh our business card design. We manufacture a range of industrial product shipping to customers internationally. A copy of our current card, both sides, is attached. We are looking for a mature professional appearance.

```html
<!DOCTYPE html>
<html lang="en">
<head>
<meta charset="utf-8">
<title>Veltrac Business Card</title>
<link href="https://fonts.googleapis.com/css2?family=Arimo:wght@400;700&display=swap" rel="stylesheet">
<style>
  :root {
    --backdrop: #3b3431;
    --card-white: #f7f7f5;
    --card-black: #111111;
    --brand-brown: #4b3c34;
    --accent-cyan: #19a7d8;
    --divider: #e2e2df;
    --silver: #d9d9d9;
    --tagline: #e6e6e6;
  }
  * { margin: 0; padding: 0; box-sizing: border-box; }
  html, body {
    width: 1200px;
    height: 844px;
    overflow: hidden;
    background: var(--backdrop);
    font-family: "Arimo", Arial, sans-serif;
  }
  .stage {
    position: relative;
    width: 1200px;
    height: 844px;
    display: flex;
    align-items: center;
    justify-content: center;
    gap: 40px;
  }
  .card {
    position: relative;
    width: 520px;
    height: 300px;
    box-shadow: 0 10px 24px rgba(0, 0, 0, 0.35);
  }

  /* Front */
  .card-front {
    background: var(--card-white);
    display: flex;
  }
  .front-brand {
    width: 205px;
    display: flex;
    flex-direction: column;
    align-items: center;
    justify-content: center;
    gap: 14px;
    border-right: 1px solid var(--divider);
    margin: 22px 0;
  }
  .brand-dot {
    width: 44px;
    height: 44px;
    border-radius: 50%;
    background: var(--accent-cyan);
  }
  .brand-name {
    font-size: 40px;
    font-weight: 700;
    color: var(--brand-brown);
    letter-spacing: -0.5px;
  }
  .front-details {
    padding: 48px 0 0 26px;
    color: var(--brand-brown);
  }
  .person-name {
    font-size: 19px;
    font-weight: 700;
    color: var(--accent-cyan);
    margin-bottom: 10px;
  }
  .contact-list {
    list-style: none;
    font-size: 13.5px;
    line-height: 18px;
  }
  .contact-list li {
    display: flex;
    align-items: center;
    gap: 8px;
  }
  .contact-icon {
    width: 12px;
    height: 12px;
    flex: none;
  }
  .address {
    margin-top: 18px;
    font-size: 14px;
    line-height: 18px;
    font-style: normal;
  }

  /* Back */
  .card-back {
    background: var(--card-black);
  }
  .back-brand {
    position: absolute;
    top: 92px;
    left: 0;
    right: 0;
    display: flex;
    flex-direction: column;
    align-items: center;
    gap: 12px;
  }
  .back-brand .brand-dot {
    background: var(--silver);
  }
  .back-brand .brand-name {
    color: var(--silver);
    font-size: 34px;
  }
  .tagline {
    position: absolute;
    left: 34px;
    right: 34px;
    bottom: 46px;
    text-align: center;
    font-size: 12px;
    letter-spacing: 0.6px;
    color: var(--tagline);
    text-transform: uppercase;
  }
</style>
</head>
<body>
<main class="stage">
  <section class="card card-front" aria-label="Business card front">
    <div class="front-brand">
      <span class="brand-dot"></span>
      <span class="brand-name">Veltrac</span>
    </div>
    <div class="front-details">
      <h1 class="person-name">Ross Kendall</h1>
      <ul class="contact-list">
        <li>
          <svg class="contact-icon" viewBox="0 0 12 12" aria-hidden="true"><rect x="1" y="5" width="10" height="6" rx="1" fill="#19a7d8"/><path d="M1 4 Q6 0 11 4 L9.5 5 Q6 3 2.5 5 Z" fill="#19a7d8"/></svg>
          +86 139 5520 0417 (China)
        </li>
        <li>
          <svg class="contact-icon" viewBox="0 0 12 12" aria-hidden="true"><rect x="1" y="5" width="10" height="6" rx="1" fill="#19a7d8"/><path d="M1 4 Q6 0 11 4 L9.5 5 Q6 3 2.5 5 Z" fill="#19a7d8"/></svg>
          +61 412 738 905 (Australia)
        </li>
        <li>
          <svg class="contact-icon" viewBox="0 0 12 12" aria-hidden="true"><rect x="0.5" y="2" width="11" height="8" rx="1" fill="#19a7d8"/><path d="M1 3 L6 7 L11 3" stroke="#f7f7f5" stroke-width="1" fill="none"/></svg>
          rkendall@veltracfittings.com
        </li>
        <li>
          <svg class="contact-icon" viewBox="0 0 12 12" aria-hidden="true"><circle cx="6" cy="6" r="5.5" fill="#19a7d8"/><ellipse cx="6" cy="6" rx="2.2" ry="5" stroke="#f7f7f5" stroke-width="0.8" fill="none"/><line x1="1" y1="6" x2="11" y2="6" stroke="#f7f7f5" stroke-width="0.8"/></svg>
          www.veltracfittings.com
        </li>
      </ul>
      <address class="address">
        1208-3, Jin Rui Building<br>
        416 Baihe Road, Haishu<br>
        District Ningbo 315010 China
      </address>
    </div>
  </section>

  <section class="card card-back" aria-label="Business card back">
    <div class="back-brand">
      <span class="brand-dot"></span>
      <span class="brand-name">Veltrac</span>
    </div>
    <p class="tagline">Hydraulic Adapters | Host Fittings | Quick Couplings</p>
  </section>
</main>
</body>
</html>
```